Wanddesign für Messeauftritt
Zielgruppe
Wir sind Werkstattausrüster für Motorrad-, PKW- und LKW-Werkstätten. Unsere Zielgruppe für diese Graphik sind zum einen Werkstattinhaber, als auch der zuständige Handel.
Aufgabenstellung
Die Graphik sollte eher schlicht gehalten sein und als Messestandwanddesign dienen.
Die hinteren beiden Wandseiten des Messestandes sollen von der Graphik abgedeckt werden.
Diese soll eher schlicht die Produkte davor glänzen lassen.
Mittig soll ein TV hängen. Wie die Gestaltung dieser Fläche aussehen soll, steht noch in den Sternen. Gerne bin ich auch hier für Ideen offen.
Gerne hätten wir unsere Farben verwendet.
C100 M85 Y0 K10
C72 M22 Y0 K0
C0 M65 Y100 K0
Maße ca. 3,25m x 2,50m je Seite
Mitte ca. 2,5m x 2,50m
Produktinfos:
www.holmbergwerkzeug.com

```html
<!DOCTYPE html>
<html lang="de">
<head>
<meta charset="utf-8">
<title>Holmberg Werkzeug – Messewand</title>
<link rel="stylesheet" href="https://fonts.googleapis.com/css2?family=Ubuntu:wght@500&family=Arimo:wght@700&display=swap">
<style>
  :root {
    --brand-navy: #1e3a8c;
    --brand-blue: #3a9fd8;
    --brand-orange: #e8731f;
    --paper: #ffffff;
    --page: #ffffff;
    --slogan: rgba(255, 255, 255, 0.38);
  }
  html, body {
    margin: 0;
    width: 1200px;
    height: 1200px;
    overflow: hidden;
    background: var(--page);
  }
  .wall {
    position: absolute;
    left: 62px;
    top: 168px;
    width: 1073px;
    height: 828px;
    overflow: hidden;
    background: linear-gradient(to bottom,
      var(--paper) 0%,
      var(--paper) 26%,
      #d3e8f6 40%,
      #7fc0e8 62%,
      var(--brand-blue) 100%);
    box-shadow: 0 2px 6px rgba(0, 0, 0, 0.25);
  }
  .wall__band {
    position: absolute;
    left: 0;
    top: 0;
    width: 100%;
    height: 50px;
    background: var(--brand-orange);
  }
  .wall__texture {
    position: absolute;
    left: 0;
    top: 250px;
    width: 100%;
    height: 578px;
    background: linear-gradient(to bottom, rgba(255,255,255,0) 0%, rgba(255,255,255,0.08) 100%);
  }
  .brand {
    position: absolute;
    left: 0;
    top: 0;
    width: 100%;
    height: 100%;
  }
  .brand__dot {
    position: absolute;
    left: 130px;
    top: 120px;
    width: 250px;
    height: 250px;
    border-radius: 50%;
    background: var(--brand-blue);
  }
  .brand__name {
    position: absolute;
    left: 440px;
    top: 62px;
    margin: 0;
    font-family: "Ubuntu", sans-serif;
    font-weight: 500;
    color: var(--brand-navy);
    font-size: 104px;
    line-height: 1;
    letter-spacing: 1px;
  }
  .brand__name span {
    display: block;
  }
  .brand__name .brand__line--small {
    font-size: 40px;
    letter-spacing: 6px;
    margin-bottom: 4px;
    margin-left: 6px;
  }
  .brand__name .brand__line--legal {
    font-size: 40px;
    letter-spacing: 10px;
    text-align: right;
    margin-top: 6px;
  }
  .slogan {
    position: absolute;
    left: 0;
    top: 0;
    margin: 0;
    width: 100%;
    height: 100%;
    font-family: "Arimo", sans-serif;
    font-weight: 700;
    color: var(--slogan);
    font-size: 152px;
    line-height: 1;
    letter-spacing: -2px;
  }
  .slogan span {
    position: absolute;
    white-space: nowrap;
  }
  .slogan__line--1 { left: 138px; top: 420px; }
  .slogan__line--2 { left: 16px;  top: 560px; }
  .slogan__line--3 { left: 466px; top: 680px; }
</style>
</head>
<body>
  <main class="wall">
    <div class="wall__band"></div>
    <div class="wall__texture" role="img" aria-label="Feines Wabenmuster aus hellen Sechsecken auf blauem Verlauf"></div>

    <p class="slogan" aria-label="holmberg engineering world">
      <span class="slogan__line--1">holmberg</span>
      <span class="slogan__line--2">engineering</span>
      <span class="slogan__line--3">world</span>
    </p>

    <header class="brand">
      <div class="brand__dot"></div>
      <h1 class="brand__name">
        <span class="brand__line--small">holmberg</span>
        <span>werkzeug</span>
        <span class="brand__line--legal">gmbh</span>
      </h1>
    </header>
  </main>
</body>
</html>
```